Home Improvement Company in need of a "Banner & Billboard Design"

I'm Looking for a Banner design 4X6 With Company Logo, Phone Number, website, Credentials and services.. I picture a charcoal/matte background i also want to look like a house shape design i will upload the sample...

I'm looking for a Billboard design to target homeowners who need Roofing Services. I need logo, number, website, KTL, Credentials and a catchy title. i will like to use the same colors for branding

Target Market(s)

Homeowners, Investors,

Industry/Entity Type

Home Improvement

Font styles to use
Decorative

Colors
00a990
5c5c5c
333333

Requirements
Must have
• All Credentials, Phone number, website, logo, logo colors, services, Eye Catchy, Direct Message, Friendly feeling,
• (614) 372 - 9058
• Roofing Gutters Painting Pressure Washing Exterior Design
Nice to have
• A catchy title, A direct message to a homeowner looking for home improvement services. noticeable
Should not have
• not Busy, no

```html
<!DOCTYPE html>
<html lang="en">
<head>
<meta charset="utf-8">
<title>Alder Peak Builders – Roofing Billboard</title>
<link href="https://fonts.googleapis.com/css2?family=Anton&family=Archivo+Black&display=swap" rel="stylesheet">
<style>
  :root{
    --brand-teal:#00a990;
    --brand-grey:#5c5c5c;
    --brand-charcoal:#333333;
    --sky-light:#6f9fd8;
    --sky-mid:#3f6fb4;
    --sky-deep:#27407e;
    --headline-blue:#1f3d8c;
    --white:#ffffff;
    --page:#ffffff;
  }
  *{margin:0;padding:0;box-sizing:border-box}
  html,body{width:1200px;height:1200px;overflow:hidden;background:var(--page)}
  .canvas{position:relative;width:1200px;height:1200px}
  .billboard{position:absolute;left:0;top:420px;width:1200px;height:360px;overflow:hidden}
  .billboard__scene{position:absolute;inset:0;
    background:
      radial-gradient(ellipse at 55% 30%, rgba(160,200,240,.55), transparent 60%),
      linear-gradient(180deg,var(--sky-mid) 0%,var(--sky-light) 45%,#4b6f9f 70%,var(--sky-deep) 100%);}
  .billboard__shade{position:absolute;inset:0;
    background:linear-gradient(90deg,rgba(30,50,110,.55) 0%,transparent 25%,transparent 80%,rgba(30,50,110,.5) 100%)}
  .headline{position:absolute;font-family:"Anton",sans-serif;color:var(--white);
    letter-spacing:1px;line-height:1;white-space:nowrap;text-transform:uppercase;
    transform:scaleX(1.31);transform-origin:left top}
  .headline--one{left:232px;top:52px;font-size:64px}
  .headline--one .lead{font-size:80px}
  .headline--one .accent{color:var(--headline-blue)}
  .headline--two{left:422px;top:162px;font-size:64px}
  .brand{position:absolute;left:36px;top:150px;width:190px;display:flex;align-items:center;gap:10px}
  .brand__mark{width:18px;height:18px;background:var(--brand-teal);flex:none}
  .brand__name{font-family:"Archivo Black",sans-serif;color:var(--brand-teal);font-size:24px;line-height:1.1}
  .bands{position:absolute;left:0;top:0;width:1200px;height:360px}
  .contact{position:absolute;font-family:"Archivo Black",sans-serif;color:var(--white);white-space:nowrap;display:flex;align-items:center;gap:8px}
  .contact--phone{left:40px;top:298px;font-size:34px}
  .contact--web{left:442px;top:306px;font-size:25px;font-variant:small-caps}
  .credential{position:absolute}
  .credential--cert{left:908px;top:276px;width:160px;height:60px;background:var(--white);border:3px solid #e6e6e6}
  .credential--accredit{left:1086px;top:216px;width:76px;height:120px;background:#1b4e9b;border:3px solid var(--white);outline:1px solid #1b4e9b}
</style>
</head>
<body>
<div class="canvas">
  <section class="billboard">
    <div class="billboard__scene" role="img" aria-label="Photo of a two-storey house with a dark tiled roof, white dormers and trees against a blue sky"></div>
    <div class="billboard__shade"></div>

    <div class="brand">
      <span class="brand__mark"></span>
      <div class="brand__name">Alder Peak Builders</div>
    </div>

    <h1 class="headline headline--one"><span class="lead">W</span>hen it comes to <span class="accent">Roofing</span></h1>
    <p class="headline headline--two">We’re on a Roll</p>

    <svg class="bands" viewBox="0 0 1200 360" aria-hidden="true">
      <polygon points="0,274 436,308 420,358 0,358" fill="var(--brand-teal)" stroke="var(--brand-charcoal)" stroke-width="3"/>
      <polygon points="422,276 876,310 862,358 420,358" fill="var(--brand-teal)" stroke="var(--brand-charcoal)" stroke-width="3"/>
    </svg>

    <div class="contact contact--phone">
      <svg width="26" height="30" viewBox="0 0 24 24" aria-hidden="true"><path fill="#fff" d="M6.6 10.8a15.1 15.1 0 0 0 6.6 6.6l2.2-2.2a1 1 0 0 1 1-.25 11.4 11.4 0 0 0 3.6.57 1 1 0 0 1 1 1V20a1 1 0 0 1-1 1A17 17 0 0 1 3 4a1 1 0 0 1 1-1h3.5a1 1 0 0 1 1 1c0 1.25.2 2.45.57 3.570a1 1 0 0 1-.25 1z"/></svg>
      (614) 372 - 9058
    </div>
    <div class="contact contact--web">
      <svg width="26" height="26" viewBox="0 0 24 24" aria-hidden="true"><g fill="none" stroke="#fff" stroke-width="1.6"><circle cx="12" cy="12" r="10"/><ellipse cx="12" cy="12" rx="4.5" ry="10"/><path d="M2 12h20M4 6.5h16M4 17.5h16"/></g></svg>
      www.AlderPeakBuilders.com
    </div>

    <div class="credential credential--cert" role="img" aria-label="Roofing contractor certification badge"></div>
    <div class="credential credential--accredit" role="img" aria-label="KTL accredited business badge"></div>
  </section>
</div>
</body>
</html>
```